Business Card for beauty technology startup

Design Glowmi Business Card for a Beauty, based on the website identity and colors (https://www.glowmi-example.com).
Glowmi is a beauty tech startup that gathers helpful product info for beauty lovers and consumers (such as availability on stores, price range and product reviews) for makeup products. The card design must be young, colorful but clean, and very modern.

Target Market(s)

woman, 15-35

Industry/Entity Type

Cosmetics

Contact Information for Business Card

Full Name, address, phone

Font styles to use
Other font styles liked:
• Advent Pro

Colors
e34297
86cfc6
ffffff
5c5c5c
e8e8e8
e667a6
b2b2b2

Requirements
Must have
• One full colored side with a creative design and another with card info
• Use Color palette: #95C5C5 and/or #D38AA5
• Use fonts: Advent Pro
• Use website identity: https://www.glowmi-example.com
Nice to have
• If needed extra font: Roboto

```html
<!DOCTYPE html>
<html lang="en">
<head>
<meta charset="utf-8">
<title>Glowmi Business Card</title>
<link href="https://fonts.googleapis.com/css2?family=Advent+Pro:wght@200;300&family=Source+Sans+3:wght@400;600&display=swap" rel="stylesheet">
<style>
  :root {
    --stage: #1b1b1b;
    --card-light: #f2f2f2;
    --card-teal: #95c5c5;
    --accent: #7cc8c8;
    --ink: #1a1a1a;
    --white: #ffffff;
  }
  * { margin: 0; padding: 0; box-sizing: border-box; }
  html, body {
    width: 1200px; height: 900px; overflow: hidden;
    background: var(--stage);
  }
  .canvas { position: relative; width: 1200px; height: 900px; }
  .card {
    position: absolute; top: 170px; width: 347px; height: 561px;
  }
  .card--front { left: 259px; background: var(--card-light); }
  .card--back { left: 631px; background: var(--card-teal); }

  .brand-ring { position: absolute; }
  .card--front .brand-ring { left: 114px; top: 68px; }
  .brand-name {
    position: absolute; left: 0; width: 100%; text-align: center;
    font-family: "Advent Pro", sans-serif; font-weight: 200;
  }
  .card--front .brand-name {
    top: 214px; font-size: 56px; letter-spacing: 9px; padding-left: 9px;
    color: var(--accent); line-height: 1;
  }

  .contact {
    position: absolute; left: 0; top: 357px; width: 100%;
    text-align: center; font-family: "Source Sans 3", sans-serif;
    color: var(--ink); font-size: 15.5px; line-height: 21px;
  }
  .contact__name {
    font-size: 22px; font-weight: 600; color: var(--accent);
    line-height: 26px; letter-spacing: 0.2px;
  }
  .contact__role { margin-bottom: 10px; }
  .contact__label { color: var(--accent); font-weight: 600; }
  .contact__web { color: var(--accent); font-weight: 600; margin-bottom: 8px; }
  .contact__address { line-height: 17px; }

  .card--back .brand-ring { left: 61px; top: 168px; }
  .card--back .brand-name {
    top: 252px; font-size: 50px; font-weight: 300;
    color: var(--white); letter-spacing: 2px; line-height: 1;
  }
</style>
</head>
<body>
<main class="canvas">
  <section class="card card--front">
    <svg class="brand-ring" width="120" height="120" viewBox="0 0 120 120" aria-hidden="true">
      <circle cx="60" cy="60" r="57" fill="none" stroke="var(--accent)" stroke-width="3"/>
    </svg>
    <div class="brand-name">GLOWMI</div>
    <div class="contact">
      <p class="contact__name">MARA ELLISON</p>
      <p class="contact__role">Managing Director</p>
      <p><span class="contact__label">P:</span> 555-014-2387</p>
      <p><span class="contact__label">E:</span> info@glowmi-example.com</p>
      <p class="contact__web">www.glowmi-example.com</p>
      <p class="contact__address">48 Petal Lane, Suite 12<br>Marbury City, 204518</p>
    </div>
  </section>

  <section class="card card--back">
    <svg class="brand-ring" width="225" height="225" viewBox="0 0 225 225" aria-hidden="true">
      <circle cx="112.5" cy="112.5" r="108" fill="none" stroke="var(--white)" stroke-width="6"/>
    </svg>
    <div class="brand-name">Glowmi</div>
  </section>
</main>
</body>
</html>
```